Dermavale "polish what the seasons left you" The whole body approach to beauty, customized skincare a

I need a stronger logo design than what I have now. I currently have a small med spa in Chicago, IL. I will be expanding my brand to New York City and the Hamptons of NY. The services I provide in Chicago include; advanced medical grade skincare treatments, laser, plastic surgery and nutrition counsel. My concept is personalized skincare. Part of my philosophy is to dedicate a lot of time and make myself always available to my clients questions and concerns. To maintain integrity of the Dermavale Philosophy I do not advertise. Dermavale is an "exclusive skincare club" therefore you must be referred by an existing client or staff member in order to get an appointment. My Chicago clientele consists of young professionals competing with their peers to look their absolute best. The New York and Hamptons business has a completely different structure. It is a Mobile med spa service providing treatments at people's homes. The services provided are advanced skincare, wellness, massage, spray tan, hair and makeup. My vision for the new logo design is to exude an image that is both cutting edge, relevant, sophisticated, sexy and modern (sleek) yet practical and strong. It must be eye catching yet simplistic, aesthetically pleasing to look at and above all must promote EXCLUSIVITY! bellow I have attached my current logo design which is printed using silver and gold foil. The other is the logo on my prescription skincare products. I need to merge the two for the brand to be cohesive. I would like to print my business cards on a mirror like material where you can see your reflection. Front of card: the brand Dermavale across the front and across the bottom will be Chicago. New York. Hamptons Back of card: in a font style like writing "Dermavale is the whole body approach to beauty. customized medical grade skincare. massage. wellness counsel. By appointment only
www.dermavalewellness-example.com p: (555) 318-2406
I am open to all suggestions to make my brand as strong as possible. Please be creative and relevant. Thank you!

```html
<!DOCTYPE html>
<html lang="en">
<head>
<meta charset="utf-8">
<title>Dermavale Wellness – Business Cards</title>
<link href="https://fonts.googleapis.com/css2?family=Open+Sans:wght@400;600;700&display=swap" rel="stylesheet">
<style>
  :root {
    --rose: #e8557a;
    --rose-deep: #d9456b;
    --graphite: #5b5b61;
    --paper: #ffffff;
    --ink-light: #fbe9ee;
    --backdrop: #e9e7e4;
  }
  * { box-sizing: border-box; margin: 0; padding: 0; }
  html, body {
    width: 1200px; height: 800px; overflow: hidden;
    background: var(--backdrop);
    font-family: "Open Sans", Arial, sans-serif;
  }
  .canvas { position: relative; width: 1200px; height: 800px; }

  .card {
    position: absolute;
    background: var(--paper);
    box-shadow: 0 6px 18px rgba(0,0,0,0.18);
    overflow: hidden;
  }

  /* Front card */
  .card--front { left: 100px; top: 255px; width: 520px; height: 300px; }
  .card__swoosh { position: absolute; inset: 0; width: 100%; height: 100%; }
  .contact {
    position: absolute; left: 26px; top: 26px; color: var(--paper);
  }
  .contact__name { font-size: 17px; font-weight: 700; letter-spacing: 0.3px; }
  .contact__role { font-size: 12px; color: var(--ink-light); margin-top: 1px; }
  .contact__address { font-size: 11px; line-height: 1.55; margin-top: 26px; color: var(--ink-light); }
  .contact__list { list-style: none; margin-top: 38px; font-size: 10.5px; line-height: 1.95; }
  .contact__list li { display: flex; align-items: center; gap: 8px; white-space: nowrap; }
  .contact__list svg { width: 11px; height: 11px; flex: none; }

  .brand {
    display: flex; align-items: center; gap: 10px;
    color: var(--graphite); font-size: 15px; font-weight: 400; letter-spacing: 0.3px;
    white-space: nowrap;
  }
  .brand__mark { width: 15px; height: 15px; background: var(--rose); flex: none; }
  .card--front .brand { position: absolute; left: 322px; top: 141px; }

  /* Back card */
  .card--back { left: 700px; top: 150px; width: 300px; height: 500px; }
  .card--back .brand {
    position: absolute; left: 50%; top: 50%;
    transform: translate(-50%, -50%) rotate(90deg);
    font-size: 18px;
  }
</style>
</head>
<body>
<main class="canvas">

  <section class="card card--front" aria-label="Business card front">
    <svg class="card__swoosh" viewBox="0 0 520 300" preserveAspectRatio="none" aria-hidden="true">
      <path d="M0 0 H316 Q258 150 292 300 H0 Z" fill="var(--graphite)"/>
      <path d="M0 0 H290 Q235 150 265 300 H0 Z" fill="var(--rose)"/>
    </svg>

    <div class="contact">
      <p class="contact__name">MARCUS ELLERY</p>
      <p class="contact__role">Managing Director</p>
      <p class="contact__address">041 12th floor, Plaza<br>Harbor Road LKG</p>
      <ul class="contact__list">
        <li>
          <svg viewBox="0 0 12 12"><path d="M3 1 L5 3.5 L4 5 Q5 7 7 8 L8.5 7 L11 9 L9.5 11 Q4 10.5 1 3 Z" fill="currentColor"/></svg>
          555 210 4478
        </li>
        <li>
          <svg viewBox="0 0 12 12"><rect x="1" y="2.5" width="10" height="7" fill="currentColor"/><path d="M1 2.5 L6 6.5 L11 2.5" stroke="var(--rose)" stroke-width="1" fill="none"/></svg>
          hello@dermavale-example.com
        </li>
        <li>
          <svg viewBox="0 0 12 12"><circle cx="6" cy="6" r="4.8" stroke="currentColor" stroke-width="1.2" fill="none"/><path d="M1.2 6 H10.8 M6 1.2 Q3 6 6 10.8 M6 1.2 Q9 6 6 10.8" stroke="currentColor" stroke-width="0.9" fill="none"/></svg>
          www.dermavalewellness-example.com
        </li>
      </ul>
    </div>

    <div class="brand"><span class="brand__mark"></span>Dermavale Wellness</div>
  </section>

  <section class="card card--back" aria-label="Business card back">
    <div class="brand"><span class="brand__mark"></span>Dermavale Wellness</div>
  </section>

</main>
</body>
</html>
```